website design for an energy technology company

Marlow Vektor Holdings is an African based company with interests in renewable energy, clean thermal power and building automation with an overall objective to ensure access to affordable, reliable, sustainable and modern energy for all.
The portal should be simple to navigate. Key attribute is to have scalable pictures of completed projects across the three different portfolios of Renewable energy, thermal power and building automation plus counters on megawatts of electricity.

Target Market(s)

Renewable energy, thermal power, building automation, smart building technology

Industry/Entity Type

Technology Equipment

Coding

Coded - Design and coding required

Number of Pages Required

5+ page

Font styles to use
Sans Serif

Colors
33a6d7
abd037
82c8e6
0255a3
33b8a4

Requirements
Must have
• Photos with human models must feature African males and females at the forefront.
We need counters on the first page and these should be represent installed base for (1) renewables-KW, (2) thermal - (kW), (3) carbon footprint saved
Nice to have
• Would like to have design that is as simple as www.qorbintel.com. With this the left hand roulette style texts will include:
Renewables - This page will now have sub menus on:
Residential Solar
Commercial building solar
Solar Rural Electrification
Windmill
Sustainable technologies

Thermal - will have sub menus like below:
Plant Operation and maintenance
Captive Power Installation

Building Automation - will have sub-menus like:
Commercial building automation
Residential Building Automation
Products
Commercial packages
Services

SDG7 News (connected to the Tz Sustainable development goals)
Blogs
In The News
Should not have
• snow, nuclear power

```html
<!DOCTYPE html>
<html lang="en">
<head>
<meta charset="utf-8">
<title>Marlow Vektor Holdings — Energy Efficiency and Sufficiency</title>
<link href="https://fonts.googleapis.com/css2?family=Mulish:wght@400;600;700;800&display=swap" rel="stylesheet">
<style>
:root{
  --teal:#1d5f70;
  --teal-dark:#174c5a;
  --accent:#2e9bd6;
  --ink:#1b1b1b;
  --text:#6a6a6a;
  --bar:#2b2f33;
  --card-dark:#2a2d31;
  --panel:#f3f3f3;
  --white:#ffffff;
}
*{box-sizing:border-box;margin:0;padding:0}
html,body{width:1200px;height:4413px;overflow:hidden;background:var(--white)}
body{font-family:'Mulish',Arial,sans-serif;color:var(--ink);position:relative}
.abs{position:absolute}
.brand{font-weight:800;color:var(--teal);font-size:26px;display:flex;align-items:center;gap:10px;line-height:1.05}
.brand .dot{width:18px;height:18px;border-radius:50%;background:var(--accent);flex:none}

/* header */
.site-header{top:0;left:0;width:1200px;height:103px;background:var(--white)}
.nav a{position:absolute;top:46px;font-size:15px;font-weight:600;color:var(--ink);text-decoration:none}
.nav a.active{color:var(--accent)}
.btn-outline{border:2px solid var(--teal);color:var(--ink);font-weight:700;font-size:17px;display:flex;align-items:center;justify-content:center;background:var(--white)}

/* hero */
.hero{top:103px;left:0;width:1200px;height:591px;background:linear-gradient(180deg,#6f6a70 0%,#8c6b5a 28%,#5a4f4a 55%,#2d2b2b 100%)}
.info-bar{top:103px;left:0;width:814px;height:51px;background:var(--bar);color:var(--white);font-size:12px;font-weight:600}
.info-bar span{position:absolute;top:18px;white-space:nowrap}
.social i{position:absolute;top:20px;width:12px;height:12px;border-radius:50%;background:var(--accent)}
.hero-title{top:262px;left:89px;width:700px;color:var(--white);font-size:51px;font-weight:700;line-height:59px;letter-spacing:.5px}
.hero-lead{top:386px;left:89px;width:480px;color:var(--white);font-size:17px;line-height:26px}
.btn-start{top:459px;left:89px;width:233px;height:59px;border:2px solid var(--white);color:var(--white);font-size:26px;display:flex;align-items:center;justify-content:center}
.play{top:459px;left:362px;width:62px;height:62px;border-radius:50%;background:radial-gradient(circle,#3fb2e0 0%,#1f86b8 70%)}

/* sections */
.section-title{font-size:35px;font-weight:700;color:var(--ink);letter-spacing:.5px}
.body-text{font-size:16px;line-height:32px;color:var(--text)}
.link-more{font-size:18px;font-weight:700;color:var(--teal);display:flex;align-items:center;gap:16px}
.link-more svg{width:22px;height:10px}

.service-card{top:984px;height:377px}
.service-photo{position:absolute;left:0;top:0;width:100%;height:100%}
.service-num{position:absolute;left:18px;font-size:42px;font-weight:600;color:rgba(255,255,255,.85)}
.service-bar{position:absolute;left:0;bottom:0;width:100%;height:53px;background:var(--teal);color:var(--white);font-weight:700;font-size:19px;display:flex;align-items:center;justify-content:space-between;padding:0 10px}
.service-panel{position:absolute;left:0;bottom:0;width:100%;height:134px;background:var(--card-dark);color:var(--white);padding:14px 16px}
.service-panel h3{font-size:19px;font-weight:600;display:flex;justify-content:space-between}
.service-panel p{font-size:14px;line-height:24px;margin-top:8px;padding-left:2px}
.service-panel .more{font-size:14px;margin-top:8px;display:flex;gap:14px;align-items:center}

.counters{top:1797px;left:146px;width:907px;height:163px;background:var(--panel);box-shadow:0 4px 12px rgba(0,0,0,.18)}
.counter{position:absolute;top:0;height:163px;text-align:center}
.counter svg{margin-top:15px;width:54px;height:60px}
.counter b{display:block;font-size:45px;color:var(--accent);font-weight:700;line-height:48px}
.counter span{display:block;font-size:17px;font-weight:600;margin-top:2px}
.divider{position:absolute;top:0;width:1px;height:163px;background:#b9b9b9}

.tile{overflow:hidden}
.tile .ph{position:absolute;inset:0}
.tile .label{position:absolute;bottom:6px;left:0;width:100%;text-align:center;color:var(--white);font-size:19px;font-weight:600;text-shadow:0 1px 3px rgba(0,0,0,.5)}

.quote-box{top:2959px;left:994px;width:117px;height:140px;background:var(--teal)}
.dots i{position:absolute;width:8px;height:8px;border-radius:50%;background:var(--ink)}
.dots i.on{width:14px;height:14px;border:2px solid var(--accent);background:var(--accent);box-shadow:inset 0 0 0 2px var(--white)}

.news-photo{top:3459px;height:335px}
.news-card{top:3732px;height:165px;background:var(--white);box-shadow:0 4px 10px rgba(0,0,0,.12);padding:24px 20px 0}
.news-card h3{font-size:19px;font-weight:600;line-height:24px}
.news-card p{font-size:14px;line-height:27px;color:var(--text);margin-top:8px;text-align:justify}
.news-date{top:3686px;width:94px;height:48px;background:var(--teal);color:var(--white);font-size:19px;font-weight:600;display:flex;align-items:center;justify-content:center}

.site-footer{top:4011px;left:0;width:1200px;height:402px;background:var(--teal);color:var(--white)}
.site-footer h4{position:absolute;top:96px;font-size:23px;font-weight:700;white-space:nowrap}
.site-footer ul{position:absolute;top:138px;list-style:none;font-size:15px;line-height:27px}
.site-footer p.small{position:absolute;font-size:15px;line-height:26px}
.email-field{top:4217px;left:850px;width:261px;height:52px;background:var(--white);color:#333;font-size:15px;display:flex;align-items:center;padding-left:8px}
.send{top:4289px;left:849px;width:156px;height:53px;border:2px solid var(--white);color:var(--white);font-size:20px;font-weight:700;display:flex;align-items:center;justify-content:center}
.copyright{top:4378px;left:0;width:1200px;text-align:center;font-size:17px;color:var(--white)}
</style>
</head>
<body>

<!-- Header -->
<header class="abs site-header">
  <div class="abs brand" style="top:22px;left:89px;width:200px"><span class="dot"></span>Marlow<br>Vektor</div>
  <nav class="nav">
    <a class="active" style="left:262px">HOME</a>
    <a style="left:341px">ABOUT US</a>
    <a style="left:456px">SERVICES</a>
    <a style="left:566px">CASE STUDIES</a>
    <a style="left:711px">BLOG</a>
    <a style="left:787px">CONTACTS</a>
  </nav>
  <div class="abs btn-outline" style="top:24px;left:962px;width:149px;height:53px">GET IN TOUCH</div>
</header>

<!-- Hero -->
<section class="abs hero" role="img" aria-label="Industrial power plant with towers and pipework at sunset"></section>
<div class="abs info-bar">
  <span style="left:89px">14 KESTREL RD, ROSEBANK, JOHANNESBURG</span>
  <span style="left:428px">+27 11 480 22 96</span>
  <span style="left:588px">info@mvh.co.za</span>
  <div class="social"><i style="left:722px"></i><i style="left:752px"></i><i style="left:786px"></i></div>
</div>
<h1 class="abs hero-title">ENERGY EFFICIENCY<br>AND SUFFICIENCY.</h1>
<p class="abs hero-lead">Lorem ipsum dolor sit amet, consectetur adipiscing elit, sed do eiusmod tempor incididunt ut labore</p>
<div class="abs btn-start">GET STARTED</div>
<div class="abs play">
  <svg width="62" height="62" viewBox="0 0 62 62"><circle cx="31" cy="31" r="12" fill="#fff"/><path d="M28 25l9 6-9 6z" fill="#1f86b8"/></svg>
</div>

<!-- Services -->
<h2 class="abs section-title" style="top:830px;left:89px">SERVICES</h2>
<p class="abs body-text" style="top:780px;left:624px;width:487px">Lorem ipsum dolor sit amet, consectetur adipiscing elit, sed do eiusmod tempor incididunt ut labore et dolore magna aliqua. Ut enim ad minim veniam, quis nostrud exercitation ullamco laboris nisi ut aliquip ex ea commodo consequat. Duis aute irure</p>
<div class="abs link-more" style="top:924px;left:625px">Explore more <svg viewBox="0 0 22 10"><path d="M0 5h19M15 1l5 4-5 4" stroke="#1d5f70" stroke-width="2" fill="none"/></svg></div>

<article class="abs service-card" style="left:89px;width:328px">
  <div class="service-photo" role="img" aria-label="Technician installing solar panels on a roof" style="background:linear-gradient(180deg,#5d97d4 0%,#89b6e2 45%,#3d4f6c 100%)"></div>
  <span class="service-num" style="top:262px">01</span>
  <div class="service-bar">RENEWABLE ENERGY <span>›</span></div>
</article>
<article class="abs service-card" style="left:437px;width:328px">
  <div class="service-photo" role="img" aria-label="Aerial view of a thermal power station beside a river" style="background:linear-gradient(180deg,#8fb3d6 0%,#4e7598 40%,#33475a 70%)"></div>
  <span class="service-num" style="top:173px">02</span>
  <div class="service-panel">
    <h3>THERMAL POWER <span style="font-size:14px">⌄</span></h3>
    <p>Lorem ipsum dolor sit amet, consectetur adipiscing elit, sed do eiusmod tempor</p>
    <div class="more">Explore more <svg width="16" height="8" viewBox="0 0 16 8"><path d="M0 4h14M11 1l3 3-3 3" stroke="#fff" stroke-width="1.5" fill="none"/></svg></div>
  </div>
</article>
<article class="abs service-card" style="left:784px;width:327px">
  <div class="service-photo" role="img" aria-label="Engineer working on a tablet with building automation icons" style="background:linear-gradient(135deg,#37556a 0%,#6e8ea2 50%,#2b3f4d 100%)"></div>
  <span class="service-num" style="top:262px">03</span>
  <div class="service-bar">BUILDING AUTOMATION <span>›</span></div>
</article>

<!-- About -->
<p class="abs body-text" style="top:1458px;left:89px;width:585px;font-size:15px;line-height:27px;text-align:justify">Lorem ipsum dolor sit amet, consectetur adipiscing elit, sed do eiusmod tempor incididunt ut labore et dolore magna aliqua. Ut enim ad minim veniam, quis nostrud exercitation</p>
<p class="abs body-text" style="top:1562px;left:89px;width:585px;font-size:15px;line-height:27px;text-align:justify">Sed ut perspiciatis unde omnis iste natus error sit voluptatem accusantium doloremque laudantium, totam rem aperiam, eaque ipsa quae ab illo inventore veritatis et quasi architecto beatae vitae dicta sunt explicabo. Nemo enim ipsam voluptatem quia voluptas sit aspernatur aut odit aut fugit, sed quia</p>
<h2 class="abs section-title" style="top:1533px;left:806px">ABOUT US</h2>
<div class="abs link-more" style="top:1688px;left:89px;gap:30px">Read more <svg viewBox="0 0 22 10"><path d="M0 5h19M15 1l5 4-5 4" stroke="#1d5f70" stroke-width="2" fill="none"/></svg></div>

<!-- Counters -->
<section class="abs counters">
  <div class="counter" style="left:0;width:310px">
    <svg viewBox="0 0 54 60" fill="none" stroke="#1d5f70" stroke-width="2"><path d="M4 58V6l24 8v44M28 14h22v44M2 58h50"/><path d="M10 18h4M18 18h4M10 26h4M18 26h4M10 34h4M18 34h4M10 42h4M18 42h4M34 22h4M42 22h4M34 30h4M42 30h4M34 38h4M42 38h4M34 46h4M42 46h4"/></svg>
    <b>50</b><span>FINIBUS BONORUM</span>
  </div>
  <div class="divider" style="left:310px"></div>
  <div class="counter" style="left:310px;width:295px">
    <svg viewBox="0 0 54 60" fill="none" stroke="#1d5f70" stroke-width="2"><circle cx="20" cy="18" r="10"/><circle cx="20" cy="18" r="4"/><path d="M20 4v4M20 28v4M6 18h4M30 18h4"/><rect x="30" y="30" width="20" height="26"/><path d="M34 38h12M34 46h12"/><circle cx="16" cy="42" r="6"/><path d="M4 58c0-8 6-10 12-10s12 2 12 10"/></svg>
    <b>700</b><span>FINIBUS BONORUM</span>
  </div>
  <div class="divider" style="left:605px"></div>
  <div class="counter" style="left:605px;width:302px">
    <svg viewBox="0 0 54 60" fill="none" stroke="#1d5f70" stroke-width="2"><path d="M4 58V30l12-8v8l12-8v8l12-8v36M2 58h50M44 58V10h6v48"/><path d="M10 40h4M20 40h4M30 40h4M10 48h4M20 48h4M30 48h4"/><path d="M46 6c2-3 6-3 6 0"/></svg>
    <b>200</b><span>FINIBUS BONORUM</span>
  </div>
</section>

<!-- Portfolios -->
<h2 class="abs section-title" style="top:2037px;left:93px">OUR PORTFOLIOS</h2>
<p class="abs body-text" style="top:2088px;left:93px;width:590px;font-size:17px;line-height:29px">Lorem ipsum dolor sit amet, consectetur adipiscing elit, sed do eiusmod tempor incididunt ut labore et dolore magna aliqua. Ut enim ad</p>
<div class="abs btn-outline" style="top:2098px;left:962px;width:149px;height:50px">VIEW MORE</div>

<div class="abs tile" style="top:2196px;left:89px;width:331px;height:346px"><div class="ph" role="img" aria-label="Solar installers fitting panels outdoors" style="background:linear-gradient(180deg,#7fa56a 0%,#4a6fa8 50%,#1f3666 100%)"></div><div class="label">RENEWABLE ENERGY</div></div>
<div class="abs tile" style="top:2196px;left:434px;width:337px;height:346px"><div class="ph" role="img" aria-label="Automated warehouse conveyor carrying boxes" style="background:linear-gradient(180deg,#a9b7c6 0%,#c9c9c5 50%,#8b8f94 100%)"></div><div class="label">BUILDING AUTOMATION</div></div>
<div class="abs tile" style="top:2196px;left:783px;width:326px;height:346px"><div class="ph" role="img" aria-label="Two colleagues reviewing a control screen" style="background:linear-gradient(135deg,#2f3c48 0%,#4f6678 55%,#1c252d 100%)"></div><div class="label">FACILITY MANAGEMENT.</div></div>
<div class="abs tile" style="top:2556px;left:89px;width:511px;height:312px"><div class="ph" role="img" aria-label="Worker installing solar modules on a roof under blue sky" style="background:linear-gradient(180deg,#2d6fbf 0%,#7ea9d7 45%,#4c5f76 100%)"></div><div class="label">INDUSTRIAL AND RESIDENTIAL SOLAR</div></div>
<div class="abs tile" style="top:2556px;left:612px;width:497px;height:312px"><div class="ph" role="img" aria-label="Wind turbines on a green hill under cloudy sky" style="background:linear-gradient(180deg,#2a68b6 0%,#a9c3df 55%,#5c7a4b 100%)"></div><div class="label">LARGE AND SMALL WIND TURBINES</div></div>

<!-- Testimonials -->
<div class="dots"><i style="top:3008px;left:92px"></i><i style="top:3008px;left:106px"></i><i class="on" style="top:3005px;left:121px"></i></div>
<h2 class="abs section-title" style="top:3012px;left:600px;width:358px;text-align:right">TESTIMONIALS</h2>
<div class="abs quote-box">
  <svg width="117" height="140" viewBox="0 0 117 140"><g fill="#fff"><path d="M36 52h16v16c0 10-5 17-12 20l-3-5c4-2 6-6 6-10h-7z"/><path d="M62 52h16v16c0 10-5 17-12 20l-3-5c4-2 6-6 6-10h-7z"/></g></svg>
</div>
<p class="abs body-text" style="top:3091px;left:129px;width:831px;font-size:15.5px;text-align:justify;text-align-last:right">Lorem ipsum dolor sit amet, consectetur adipiscing elit, sed do eiusmod tempor incididunt ut labore et dolore magna aliqua. Ut enim ad minim veniam, quis nostrud exercitation ullamco laboris nisi ut aliquip ex ea commodo consequat. Duis aute irure dolor in reprehenderit in voluptate velit esse cillum dolore eu nulla pariatur. Excepteur sint occaecat cupidatat non proident, sunt in culpa qui officia deserunt mollit anim id est</p>
<div class="abs" style="top:3232px;left:727px;font-size:21px;font-weight:600;color:#333">Tendai, <span style="color:var(--accent)">CEO</span></div>
<div class="abs" style="top:3245px;left:869px;width:88px;height:2px;background:var(--accent);opacity:.6"></div>

<!-- News -->
<h2 class="abs section-title" style="top:3380px;left:0;width:1200px;text-align:center">NEWS</h2>

<div class="abs news-photo" style="left:91px;width:329px;background:radial-gradient(circle at 55% 45%,#f6d56a 0%,#a2862e 35%,#3a5a1e 75%)" role="img" aria-label="Glowing light bulb beside a young plant"></div>
<div class="abs news-photo" style="left:437px;width:329px;background:linear-gradient(135deg,#5e6670 0%,#b0b5ba 50%,#4c5259 100%)" role="img" aria-label="Engineer in hard hat with laptop in a plant room"></div>
<div class="abs news-photo" style="left:782px;width:329px;background:linear-gradient(180deg,#8aa0b6 0%,#d2d6da 50%,#6b7b86 100%)" role="img" aria-label="Automated production line with machinery"></div>

<article class="abs news-card" style="left:99px;width:316px"><h3>FINIBUS BONORUM ET MALORUM</h3><p>Sed ut perspiciatis unde omnis iste natus error sit voluptatem accusantium doloremque laudantium, totam</p></article>
<article class="abs news-card" style="left:443px;width:318px"><h3>FINIBUS BONORUM ET MALORUM</h3><p>Sed ut perspiciatis unde omnis iste natus error sit voluptatem accusantium doloremque laudantium, totam</p></article>
<article class="abs news-card" style="left:787px;width:319px"><h3>FINIBUS BONORUM ET MALORUM</h3><p>Sed ut perspiciatis unde omnis iste natus error sit voluptatem accusantium doloremque laudantium, totam</p></article>
<div class="abs news-date" style="left:300px">7-01-20</div>
<div class="abs news-date" style="left:647px">10-01-20</div>
<div class="abs news-date" style="left:992px">15-01-20</div>

<div class="dots"><i style="top:3940px;left:581px"></i><i class="on" style="top:3937px;left:594px"></i><i style="top:3940px;left:613px"></i></div>

<!-- Footer -->
<footer class="abs site-footer">
  <div class="abs brand" style="top:46px;left:91px;color:#fff"><span class="dot" style="background:#fff"></span>Marlow<br>Vektor</div>
  <p class="small" style="top:146px;left:91px;width:280px">Lorem ipsum dolor sit amet, consectetur adipiscing elit, sed do eiusmod tempor incididunt ut</p>
  <h4 style="left:405px">QUICKS LINKS</h4>
  <ul style="left:406px"><li>Home</li><li>About Us</li><li>Services</li><li>Case Studies</li><li>Blog</li><li>Contacts</li></ul>
  <h4 style="left:619px">SERVICES</h4>
  <ul style="left:621px"><li>Renewable energy</li><li>Thermal power</li><li>Building Automation</li></ul>
  <h4 style="left:849px">SIGN UP TO MVH</h4>
  <p class="small" style="top:151px;left:851px;width:240px;line-height:22px">Lorem ipsum dolor sit amet, consectetur adipiscing elit</p>
</footer>
<div class="abs email-field">Enter the Email</div>
<div class="abs send">Send</div>
<div class="abs copyright">© Copyright 2020 Marlow Vektor Holdings. All Rights Reserved</div>

</body>
</html>
```